Icons for each step of my seven step process

Hi, I run a business coaching service for dentists. I have a 7 step process I take my clients through. I need to create an icon for each of my steps.
I also need to create an info graphic that relates these 7 steps in a process ie one leading to the other and then ending up back at the beginning.
I'm also looking to possibly add an 8th step and would like an icon for that too as well as an info graphic showing the 8 steps please.
From a style point of view I like the look of BrellowNotes.com. My website will be clean looking and I'd like the icons to be clean looking as well. I'm happy for an array of colours to be used as well. I DO NOT want any icons with teeth or dental specific images. These icons should describe the process not the market.
I'd like the icon enclosed. I do like the rounded corners type of design often associated with apps but I'm open to other shapes as well.
I'd like the icons to have a professional feel but still look "cool and groovy"
The icons should not be numbered either please.
The seven / eight steps are:
1. Foundations
2. Building a high performance team
3. Operating Systems
4. Financial Systems
5. Case Acceptance (this is essentially a sales process - no shopping cart icons though please)
6. WOW customer service
7. Marketing
8. Creating Balance (not a yin yang please)
I'm happy if you need to abbreviate some of these points to a single word or two EG Team.
Many thanks,
Marty
Updates
Target Market(s)
Dentists
Industry/Entity Type
Shopping
Requirements
Must have
- Enclosed images for the icons but not necessarily for the infogrpahic.
Professional looking but still look cool / arty / groovy
Modern font.
Nice to have
- See BrellowNotes.com for inspiration.
Should not have
- No illustrations of "shopping carts" for case acceptance and no illustrations of "yin yang's" for balance.
No old style fancy / flowery fonts.
No metallic type or reflective icons please.

```html
<!DOCTYPE html>
<html lang="en">
<head>
<meta charset="utf-8">
<title>Seven-step coaching cycle</title>
<link href="https://fonts.googleapis.com/css2?family=Open+Sans:ital,wght@0,700;1,700&display=swap" rel="stylesheet">
<style>
  :root {
    --step-yellow: #fdcb33;
    --step-yellow-soft: #fedb6e;
    --icon-white: #ffffff;
    --canvas-bg: #ffffff;
  }
  html, body { margin: 0; padding: 0; overflow: hidden; background: var(--canvas-bg); }
  .canvas { width: 1200px; height: 1000px; position: relative; overflow: hidden; }
  .cycle { display: block; width: 1200px; height: 1000px; }
  .step-disc { fill: var(--step-yellow); }
  .icon-fill { fill: var(--icon-white); }
  .icon-stroke { stroke: var(--icon-white); fill: none; }
  .connector { stroke: var(--step-yellow); stroke-width: 4; fill: none; }
  .arrowhead { fill: var(--step-yellow); }
  .dollar-sign { font-family: "Open Sans", Arial, sans-serif; font-weight: 700; font-size: 92px; fill: var(--icon-white); }
  .wow-label { font-family: "Open Sans", Arial, sans-serif; font-style: italic; font-weight: 700; font-size: 17px; fill: var(--step-yellow); letter-spacing: 1px; }
  .team-placeholder { fill: var(--step-yellow-soft); }
</style>
</head>
<body>
<div class="canvas">
<svg class="cycle" viewBox="0 0 1200 1000" xmlns="http://www.w3.org/2000/svg" aria-label="Eight-step process cycle">
  <defs>
    <marker id="arrow-tip" viewBox="0 0 10 10" refX="2" refY="5" markerWidth="6" markerHeight="6" orient="auto" markerUnits="strokeWidth">
      <path class="arrowhead" d="M0,0 L10,5 L0,10 Z"/>
    </marker>
  </defs>

  <!-- connectors -->
  <g class="connectors">
    <path class="connector" marker-end="url(#arrow-tip)" d="M444,230 Q475,206 510,196"/>
    <path class="connector" marker-end="url(#arrow-tip)" d="M704,218 Q742,230 768,248"/>
    <path class="connector" marker-end="url(#arrow-tip)" d="M886,380 Q905,414 911,446"/>
    <path class="connector" marker-end="url(#arrow-tip)" d="M884,627 Q871,670 853,696"/>
    <path class="connector" marker-end="url(#arrow-tip)" d="M707,800 Q672,816 636,820"/>
    <path class="connector" marker-end="url(#arrow-tip)" d="M471,806 Q435,794 406,772"/>
    <path class="connector" marker-end="url(#arrow-tip)" d="M307,640 Q291,604 288,574"/>
    <path class="connector" marker-end="url(#arrow-tip)" d="M298,407 Q305,370 320,344"/>
  </g>

  <!-- Foundations -->
  <g class="step step-foundations" transform="translate(615,204)">
    <circle class="step-disc" r="67"/>
    <rect class="icon-fill" x="-46" y="2" width="35" height="18"/>
    <rect class="icon-fill" x="-8" y="2" width="35" height="18"/>
    <rect class="icon-fill" x="30" y="2" width="25" height="18"/>
    <rect class="icon-fill" x="-37" y="-18" width="35" height="17"/>
    <rect class="icon-fill" x="1" y="-18" width="35" height="17"/>
    <rect class="icon-fill" x="-18" y="-38" width="35" height="17"/>
  </g>

  <!-- Team -->
  <g class="step step-team" transform="translate(850,314)">
    <circle class="step-disc" r="67"/>
    <rect class="team-placeholder" x="-52" y="-46" width="104" height="72" rx="6" role="img" aria-label="Team icon: three figures standing together"/>
  </g>

  <!-- Operating systems -->
  <g class="step step-operations" transform="translate(912,550)">
    <circle class="step-disc" r="72"/>
    <circle class="icon-stroke" cx="-18" cy="-12" r="30" stroke-width="6" stroke-dasharray="3.5 3"/>
    <circle class="icon-fill" cx="-18" cy="-12" r="25"/>
    <circle class="step-disc" cx="-18" cy="-12" r="9"/>
    <circle class="icon-fill" cx="-18" cy="-12" r="6"/>
    <circle class="icon-stroke" cx="29" cy="22" r="19" stroke-width="5" stroke-dasharray="3 2.6"/>
    <circle class="icon-fill" cx="29" cy="22" r="15"/>
    <circle class="step-disc" cx="29" cy="22" r="6"/>
    <circle class="icon-fill" cx="29" cy="22" r="4"/>
  </g>

  <!-- Financial systems -->
  <g class="step step-finance" transform="translate(779,761)">
    <circle class="step-disc" r="72"/>
    <text class="dollar-sign" x="0" y="33" text-anchor="middle">$</text>
  </g>

  <!-- Case acceptance -->
  <g class="step step-acceptance" transform="translate(546,814)">
    <circle class="step-disc" r="68"/>
    <path class="icon-fill" d="M-45,6 L-26,18 Q-5,-26 37,-42 Q0,-12 -17,40 Z"/>
  </g>

  <!-- WOW service -->
  <g class="step step-service" transform="translate(340,708)">
    <circle class="step-disc" r="68"/>
    <ellipse class="icon-fill" cx="-3" cy="-3" rx="48" ry="29" transform="rotate(8)"/>
    <path class="icon-fill" d="M28,12 Q38,28 48,36 Q28,36 18,24 Z"/>
    <text class="wow-label" x="-4" y="2" text-anchor="middle" transform="rotate(8)">wow</text>
  </g>

  <!-- Marketing -->
  <g class="step step-marketing" transform="translate(288,479)">
    <circle class="step-disc" r="68"/>
    <polygon class="icon-fill" points="0,-41 10,-16 39,-14 17,5 24,33 0,19 -24,33 -17,5 -39,-14 -10,-16"/>
  </g>

  <!-- Creating balance -->
  <g class="step step-balance" transform="translate(389,279)">
    <circle class="step-disc" r="68"/>
    <rect class="icon-fill" x="-28" y="29" width="56" height="4"/>
    <rect class="icon-fill" x="-3" y="-30" width="6" height="60"/>
    <path class="icon-fill" d="M0,-42 L3,-30 L-3,-30 Z"/>
    <path class="icon-stroke" stroke-width="3" d="M-36,-20 L0,-30 L36,-20"/>
    <path class="icon-stroke" stroke-width="2" d="M-36,-20 L-48,6 M-36,-20 L-24,6 M36,-20 L24,6 M36,-20 L48,6"/>
    <path class="icon-fill" d="M-50,6 Q-36,18 -22,6 Z"/>
    <path class="icon-fill" d="M22,6 Q36,18 50,6 Z"/>
  </g>
</svg>
</div>
</body>
</html>
```